Navory - макеты для постов в VK и TG
Задание на дизайн
Какой товар или услуга будет рекламироваться?
сервис по продаже недвижимости (квартиры)
макеты для TG vk
использованы будут для публикации в группе / канале сервиса, а так же для рекламного продвижения согласно контент плану
темы контент плана:
Пост 1. «Комиссия риелтора — это как скрытый налог»
Пост 2. «Риелтор ≠ маг и волшебник»
Пост 3. «Кто работает — вы или риелтор?»
Пост 4. «Риелтору выгодно, чтобы вы продали дешевле»
Пост 5. «Юридические риски: риелтор не всегда спасает»
Пост 6. «Риелтор как такси за миллион»
желательно что бы макеты содержали элементы фирменного стиля (шрифт, цвет ..)
https://files.pelmaroshare.net/folders/7kq48TzrbnLeoXvamPsUdcQwyhiFJRt_?usp=share_link
задача: пользователь должен заинтересоваться макетом и пойти читать полный объем текста, желательно еще и подписался
На каких сайтах будет размещаться баннер
vk, tg
Размер баннера
600 px × 600 px
Тип баннера
Статический

```html
<!DOCTYPE html>
<html lang="ru">
<head>
<meta charset="utf-8">
<title>Navory — Риелтор как такси за миллион</title>
<link href="https://fonts.googleapis.com/css2?family=Jost:wght@400;500&display=swap" rel="stylesheet">
<style>
  :root {
    --bg: #e4eae5;
    --ring: #f3f6f3;
    --brand: #3f9a6e;
    --ink: #111111;
    --photo-sky: #eef0f1;
    --photo-facade: #cfd4d7;
    --photo-glass: #5f6b74;
    --photo-shirt: #9ea3a6;
    --photo-denim: #2e3d57;
  }
  html, body {
    margin: 0;
    padding: 0;
    width: 1200px;
    height: 1200px;
    overflow: hidden;
    background: var(--bg);
  }
  .post {
    position: relative;
    width: 1200px;
    height: 1200px;
    background: var(--bg);
    font-family: "Jost", "Helvetica Neue", Arial, sans-serif;
    overflow: hidden;
  }
  .post__rings {
    position: absolute;
    inset: 0;
  }
  .brand {
    position: absolute;
    left: 36px;
    top: 22px;
    color: var(--brand);
  }
  .brand__name {
    font-size: 66px;
    font-weight: 400;
    line-height: 1;
    letter-spacing: 1px;
  }
  .brand__tagline {
    margin-top: 10px;
    font-size: 12.5px;
    font-weight: 400;
    letter-spacing: 0.6px;
    text-transform: uppercase;
  }
  .post__photo {
    position: absolute;
    left: 160px;
    top: 10px;
    width: 880px;
    height: 880px;
    border-radius: 50%;
    background:
      radial-gradient(ellipse 32% 55% at 52% 62%, rgba(70, 76, 82, 0.55) 0%, rgba(70, 76, 82, 0) 100%),
      linear-gradient(180deg,
        var(--photo-sky) 0%,
        var(--photo-facade) 18%,
        var(--photo-glass) 34%,
        var(--photo-facade) 46%,
        var(--photo-shirt) 60%,
        var(--photo-glass) 76%,
        var(--photo-denim) 92%,
        var(--photo-denim) 100%);
  }
  .headline {
    position: absolute;
    left: 270px;
    top: 952px;
    margin: 0;
    color: var(--ink);
    font-size: 84px;
    font-weight: 400;
    line-height: 98px;
    letter-spacing: 0;
    text-transform: uppercase;
    white-space: nowrap;
    transform: scaleX(0.74);
    transform-origin: left top;
  }
</style>
</head>
<body>
  <main class="post">
    <svg class="post__rings" width="1200" height="1200" viewBox="0 0 1200 1200" aria-hidden="true">
      <g fill="none" stroke="var(--ring)" stroke-width="2">
        <circle cx="600" cy="450" r="530"/>
        <circle cx="600" cy="450" r="650"/>
        <circle cx="600" cy="450" r="790"/>
        <circle cx="600" cy="450" r="950"/>
      </g>
    </svg>

    <div class="brand">
      <div class="brand__name">navory</div>
      <div class="brand__tagline">Сервис по продаже недвижимости</div>
    </div>

    <div class="post__photo" role="img" aria-label="Фото: расстроенный мужчина в клетчатой рубашке и джинсах говорит по телефону, прижав ладонь ко лбу, на фоне современного стеклянного здания"></div>

    <h1 class="headline">Риелтор как такси<br>за миллион</h1>
  </main>
</body>
</html>
```